Global Leadership Company requires banner design

I need 3 large banners designed. i will be using these for advertising and also a condensed version as the header on a splash pages.

I have attached the wording and also the photo's that i'd like used in each design.
Note: i've just placed the wording randomly, you'll have to place it where it makes the most sense for the message and the design.

I want something with bright colors that pops.

Reason: I'd like to give the most recent designers time to submit quality work.

```html
<!DOCTYPE html>
<html lang="en">
<head>
<meta charset="utf-8">
<title>Personal Empowerment Banners</title>
<link href="https://fonts.googleapis.com/css2?family=Archivo+Black&family=Lilita+One&family=PT+Sans:ital,wght@0,400;0,700;1,700&family=Titillium+Web:wght@700&display=swap" rel="stylesheet">
<style>
:root{
  --blue:#2323e6;
  --navy:#141a8c;
  --deep:#0c1a6e;
  --red:#ee1111;
  --yellow:#ffff22;
  --gold:#f4e02a;
  --panel:#ececf0;
  --lavender:#a6a4f6;
  --ink:#333340;
  --white:#ffffff;
  --photo-a:#c9a77e;
  --photo-b:#6b4a35;
}
*{margin:0;padding:0;box-sizing:border-box}
html,body{width:1200px;height:1120px;overflow:hidden;background:var(--white)}
body{position:relative;font-family:"PT Sans",Arial,sans-serif}
.banner{position:absolute;left:46px;width:1136px;height:342px;background:var(--panel)}
.banner-one{top:24px;border:4px solid var(--blue);box-shadow:inset 0 0 0 4px var(--white),inset 0 0 0 6px #b8b8c8}
.banner-two{top:392px;border:7px solid var(--yellow);box-shadow:0 0 0 2px #d8d040}
.banner-three{top:757px;border:7px solid var(--blue)}
.abs{position:absolute}
.center{text-align:center;left:0;right:0}
.wanted{top:8px;font-family:"Archivo Black",sans-serif;font-size:37px;color:var(--red);-webkit-text-stroke:1.5px #7a1a00;text-shadow:0 0 3px var(--yellow),0 0 2px var(--yellow);letter-spacing:1px;line-height:1}
.driven{top:46px;font-family:"Archivo Black",sans-serif;font-size:24px;color:var(--white);text-shadow:-1px -1px 0 #222,1px -1px 0 #222,-1px 1px 0 #222,1px 1px 0 #222,2px 2px 2px #555;line-height:1.2}
.driven .ready{color:var(--red)}
.boom{top:78px;font-family:"Titillium Web",sans-serif;font-size:24px;color:var(--blue);line-height:1.2}
.testimonial{left:20px;top:110px;width:332px;height:222px;background:var(--lavender)}
.photo{background:radial-gradient(ellipse at 50% 40%,var(--photo-a),var(--photo-b))}
.oval{left:16px;top:108px;width:168px;height:226px;border-radius:50%;border:4px solid var(--yellow)}
.quote-red{left:190px;top:130px;width:158px;font-style:italic;font-weight:700;font-size:23px;line-height:1.15;color:var(--red);text-align:center}
.signed{left:190px;top:300px;width:158px;text-align:center;color:var(--white);font-size:18px}
.claim{left:362px;top:112px;width:756px;height:72px;border:2px solid var(--yellow);background:var(--white);color:var(--blue);font-style:italic;font-weight:700;font-size:23px;line-height:1.2;text-align:center;padding-top:6px}
.point{font-family:"Titillium Web",sans-serif;font-size:25px;color:var(--ink);white-space:nowrap;line-height:1}
.launch{left:372px;top:278px;font-family:"Lilita One",sans-serif;font-size:24px;color:var(--yellow);-webkit-text-stroke:1px #3a3a00;white-space:nowrap}
.cta{display:flex;align-items:center;justify-content:center;text-align:center;font-family:"Lilita One",sans-serif;line-height:1.1}
.cta-gold{left:758px;top:266px;width:356px;height:54px;background:linear-gradient(#fffe70,var(--gold) 55%,#d9b800);border:2px solid #c8a400;border-radius:4px;color:var(--navy);font-size:24px;letter-spacing:1px;box-shadow:2px 3px 3px rgba(0,0,0,.4)}
.cta-blue{background:linear-gradient(#7a7cf5,var(--blue) 55%,#1616a8);border:2px solid #0e0e80;border-radius:12px;color:var(--yellow);box-shadow:2px 3px 4px rgba(0,0,0,.45)}
.cta-two{left:868px;top:255px;width:244px;height:66px;font-size:24px}
.cta-three{left:808px;top:228px;width:300px;height:80px;font-size:30px}
.head-box{left:166px;top:4px;width:952px;height:138px;border:2px solid var(--blue);border-radius:22px;background:var(--panel)}
.head-line{font-family:"Lilita One",sans-serif;font-size:24px;color:var(--yellow);-webkit-text-stroke:1px #333300;white-space:nowrap}
.circle{border-radius:50%;border:5px solid var(--blue)}
.circle-two{left:4px;top:20px;width:272px;height:300px}
.point-blue{font-family:"Lilita One",sans-serif;font-size:23px;color:var(--blue);white-space:nowrap}
.quote-box{left:274px;top:246px;width:588px;height:70px;border-radius:12px;background:var(--blue);color:var(--yellow);font-family:"Lilita One",sans-serif;font-size:22px;line-height:1.3;text-align:center;padding-top:4px}
.title-pill{left:202px;top:4px;width:740px;height:52px;border:3px solid var(--yellow);border-radius:26px;background:var(--panel);font-family:"Archivo Black",sans-serif;font-size:33px;color:var(--navy);text-align:center;line-height:46px;text-shadow:1px 1px 0 var(--white)}
.circle-three{left:10px;top:46px;width:272px;height:274px}
.caps{left:270px;width:520px;text-align:center;font-size:24px;color:var(--deep);text-transform:uppercase;letter-spacing:.5px;white-space:nowrap}
.benefits{left:870px;top:80px;list-style:none}
.benefits li{font-size:24px;color:var(--blue);text-transform:uppercase;line-height:32px;white-space:nowrap}
.benefits li::before{content:"";display:inline-block;width:11px;height:11px;border-radius:50%;background:var(--blue);margin-right:10px;vertical-align:3px}
.formula{left:252px;top:226px;width:500px;height:84px;border-radius:12px;background:var(--blue);font-family:"Lilita One",sans-serif;font-size:25px;line-height:1.3;text-align:center;padding-top:6px;color:var(--yellow)}
.formula .plain{color:var(--white)}
</style>
</head>
<body>

<section class="banner banner-one">
  <div class="abs center wanted">WANTED</div>
  <div class="abs center driven">driven individuals <span class="ready">READY</span> to take their results to the next level</div>
  <div class="abs center boom">Personal Empowerment..... the NEXT Big Business Boom!</div>
  <div class="abs testimonial"></div>
  <div class="abs oval photo" role="img" aria-label="Portrait photo of a smiling woman with long blonde hair"></div>
  <p class="abs quote-red">“Within just 5 months I was making over $25,000 per month”</p>
  <p class="abs signed">Dana, Colorado</p>
  <p class="abs claim">“Let us show you how we’ve taught average people to earn an executives salary from home – part time. FAST!”</p>
  <span class="abs point" style="left:380px;top:190px">- Make up to $5,000 per sale</span>
  <span class="abs point" style="left:802px;top:190px">- No experience required</span>
  <span class="abs point" style="left:380px;top:232px">- No cold calling</span>
  <span class="abs point" style="left:662px;top:232px">- NOT MLM</span>
  <span class="abs point" style="left:846px;top:232px">- No pressure selling</span>
  <span class="abs launch">Just launched in United States</span>
  <a class="abs cta cta-gold">CLICK HERE FOR FREE INFO</a>
</section>

<section class="banner banner-two">
  <div class="abs head-box"></div>
  <span class="abs head-line" style="left:270px;top:18px">Passionate about Personal Development / Leadership Development?</span>
  <span class="abs head-line" style="left:320px;top:60px">Looking to align yourself with an opportunity of substance?</span>
  <span class="abs head-line" style="left:346px;top:102px">Ready to be challenged &amp; encouraged to reach new level’s of success?</span>
  <div class="abs circle circle-two photo" role="img" aria-label="Photo of a smiling couple, the man in a tuxedo and the woman with blonde hair"></div>
  <span class="abs point-blue" style="left:340px;top:158px">- Home Based</span>
  <span class="abs point-blue" style="left:622px;top:158px">- NOT MLM</span>
  <span class="abs point-blue" style="left:858px;top:158px">- No Cold Calling</span>
  <span class="abs point-blue" style="left:344px;top:206px">- Simple Success Formula</span>
  <span class="abs point-blue" style="left:692px;top:208px">- Opportunity for “Big Thinker”</span>
  <p class="abs quote-box">“Let us show you how we’ve taught others like you<br>to make a quantum leap in their personal results”</p>
  <a class="abs cta cta-blue cta-two">CLICK HERE FOR<br>FREE INFO</a>
</section>

<section class="banner banner-three">
  <h1 class="abs title-pill">Change Your Tomorrow – TODAY!</h1>
  <div class="abs circle circle-three photo" role="img" aria-label="Photo of a smiling couple posing close together"></div>
  <p class="abs caps" style="top:80px">Learn to turn your spare time into</p>
  <p class="abs caps" style="top:110px">an executive level income</p>
  <p class="abs caps" style="top:154px">In just 2 hours per day you can make a</p>
  <p class="abs caps" style="top:194px">quantum leap in your results</p>
  <ul class="abs benefits">
    <li>More time</li>
    <li>More fulfillment</li>
    <li>More money</li>
    <li>More fun</li>
  </ul>
  <p class="abs formula">Learn our success formula <span class="plain">TODAY</span><br><span class="plain">so you can enjoy more</span> TOMORROW</p>
  <a class="abs cta cta-blue cta-three">CLICK HERE FOR<br>FREE INFO</a>
</section>

</body>
</html>
```